Need Wordpress website design for tutoring service startup

We are a tutoring service out of Tucson, Arizona, called 'Harbor Scholars LLC,' and we are looking for a website that communicates academic success but doesn't take itself too seriously. The website should have artistic themes inspired by the Sonoran desert (or nature in general) and the great horned owl. Our main goal is to help students get the grades they want. We want to be a trusted provider of academic help to those who need it.
We provide all subject tutoring (including exam prep), mainly for high school and undergraduate college students. The client would only pay for the time they spend with their tutor - no tutoring packages. The tutors can set their prices. Both online and In-person tutoring is available. I want this website to be compatible with the tutoring software we're using, lessonkite (lessonkite.example).
Pages we need - Home, Subjects, Our Team and Tutors, FAQs, Be a Tutor, Contact.
I want a Testimonials section somewhere on the home page.
Websites I like:
studyforallfolk.example
jarblue.example
mentorlens.example
My competitors:
scimasterycoaching.example
dorvanhomecoaching.example
This is my first time using artmarket, so I hope this is a good brief. Let me know if you need more details.
Target Market(s)
Highschool students, college students, and the parents of those students
Coding
Coded - Design and coding required
Look and feel

```html
<!DOCTYPE html>
<html lang="en">
<head>
<meta charset="utf-8">
<title>Harbor Scholars LLC – Tutoring in Tucson</title>
<link rel="stylesheet" href="https://fonts.googleapis.com/css2?family=Montserrat:wght@500;600;700;800&family=Roboto:ital,wght@0,400;0,500;0,700;1,400&display=swap">
<style>
:root{
  --orange:#e07b2f;
  --orange-deep:#d9702a;
  --yellow:#f6be3c;
  --brown:#3a2318;
  --brown-mid:#5a3620;
  --ink:#1f1f1f;
  --text:#555;
  --muted:#ececec;
  --white:#fff;
}
*{box-sizing:border-box;margin:0;padding:0}
html,body{width:1200px;height:4626px;overflow:hidden}
body{position:relative;background:var(--white);font-family:'Roboto',sans-serif;color:var(--text)}
.abs{position:absolute}
h1,h2,h3,h4{font-family:'Montserrat',sans-serif}

/* header */
.brand{left:115px;top:10px;display:flex;align-items:center;gap:10px;z-index:2}
.brand-dot{width:44px;height:44px;border-radius:50%;background:var(--orange)}
.brand-name{font-family:'Montserrat',sans-serif;font-weight:600;font-size:22px;line-height:24px;color:var(--brown)}
.nav{left:378px;top:40px;display:flex;gap:24px;font-size:14px;font-weight:500;color:#444;z-index:2}
.nav a{color:inherit;text-decoration:none;padding-bottom:6px}
.nav a.active{color:var(--orange);border-bottom:3px solid var(--orange)}
.call-btn{left:903px;top:26px;width:186px;height:46px;border-radius:23px;background:linear-gradient(90deg,var(--orange),var(--yellow));color:#fff;font-size:14px;font-weight:500;display:flex;align-items:center;justify-content:center;gap:8px;z-index:2}

.hero-box{left:275px;top:225px;width:650px;height:260px;background:rgba(120,110,100,.55);text-align:center;color:#fff}
.hero-box .kicker{font-family:'Montserrat',sans-serif;font-weight:500;font-size:26px;margin-top:45px;letter-spacing:.5px}
.hero-box h1{font-weight:700;font-size:50px;margin-top:8px}
.btn{display:inline-flex;align-items:center;gap:8px;height:44px;padding:0 28px;border-radius:22px;background:linear-gradient(90deg,var(--orange),var(--yellow));color:#fff;font-family:'Montserrat',sans-serif;font-weight:700;font-size:13px}
.hero-box .btn{margin-top:22px}

/* story */
.story-text{left:598px;top:785px;width:490px}
.story-text h2{font-size:42px;font-weight:700;color:var(--ink)}
.story-sub{margin-top:28px;border-left:5px solid var(--orange);padding-left:20px;font-family:'Montserrat',sans-serif;font-weight:700;font-size:20px;line-height:34px;color:var(--ink)}
.story-text p{margin-top:24px;font-size:13.5px;line-height:25.5px;text-align:justify}
.story-text .btn{margin-top:30px}
.vertical-word{font-family:'Montserrat',sans-serif;font-weight:800;color:var(--muted);writing-mode:vertical-rl;letter-spacing:2px}

/* why */
.why-card{background:#fff;padding:16px 26px;box-shadow:0 6px 18px rgba(0,0,0,.12);z-index:1}
.why-card h3{font-weight:600;font-size:20px;color:var(--orange)}
.why-card p{margin-top:10px;font-size:13.5px;line-height:25.5px;text-align:justify}
.why-center{background:var(--orange);color:#fff;font-family:'Montserrat',sans-serif;font-weight:700;font-size:26px;line-height:46px;text-align:center;display:flex;align-items:center;justify-content:center;z-index:2}

.section-title{width:1200px;left:0;text-align:center}
.section-title .ghost{font-family:'Montserrat',sans-serif;font-weight:700;font-size:80px;color:#ededed;line-height:1}
.section-title h2{position:absolute;left:0;right:0;font-weight:700;font-size:44px;color:var(--ink)}

/* services */
.svc{width:325px;height:310px;text-align:center;color:#fff}
.svc h3{font-weight:600;font-size:20px;color:#fff}
.svc p{margin-top:14px;font-size:13.5px;line-height:25.5px;padding:0 42px}
.svc .go{margin:20px auto 0;width:18px;height:18px}
.icon-ring{width:92px;height:92px;border-radius:50%;background:#fff;box-shadow:0 4px 12px rgba(0,0,0,.15);display:flex;align-items:center;justify-content:center;z-index:2}

/* testimonials */
.t-card{width:475px;height:250px;background:#fff;padding:20px 24px;box-shadow:0 6px 20px rgba(0,0,0,.12)}
.t-head{display:flex;align-items:center;gap:18px}
.avatar{width:88px;height:88px;border-radius:50%;background:radial-gradient(circle at 50% 40%,#c9a891,#7a5a46 65%,#e9e4df 66%)}
.t-head h4{font-weight:600;font-size:22px;color:var(--orange)}
.t-head span{display:block;font-family:'Montserrat',sans-serif;font-weight:600;font-size:16px;color:#333;margin-top:8px}
.t-card p{margin-top:22px;font-style:italic;font-size:13.5px;line-height:25.5px}
.quote-mark{right:20px;top:12px;font-family:'Montserrat',sans-serif;font-weight:800;font-size:130px;line-height:1;color:#e4e4e4}

/* team */
.member{width:260px;text-align:center}
.member .portrait{width:244px;height:244px;border-radius:50%;margin:0 auto;border-bottom:9px solid var(--yellow)}
.member h3{margin-top:30px;font-weight:600;font-size:26px;color:var(--ink)}
.member span{display:block;margin-top:12px;font-family:'Montserrat',sans-serif;font-weight:600;font-size:20px;color:#555}

/* footer */
.foot-col h4{font-family:'Roboto',sans-serif;font-weight:500;font-size:15px;color:#fff;letter-spacing:.3px}
.foot-col ul{list-style:none;margin-top:20px}
.foot-col li{font-size:12.5px;color:#f1e6dc;line-height:26px;display:flex;align-items:flex-start;gap:10px}
.foot-col li svg{flex:none;margin-top:7px}
.soc{width:30px;height:30px;border-radius:50%;background:var(--yellow);flex:none}
.foot-col .soc-list li{align-items:center;line-height:34px}
.copyright{left:0;width:1200px;top:4574px;text-align:center;font-size:12.5px;color:#f1e6dc}
</style>
</head>
<body>

<!-- hero -->
<svg class="abs" style="left:0;top:0" width="1200" height="740" viewBox="0 0 1200 740">
  <defs>
    <linearGradient id="heroTone" x1="0" y1="0" x2="1" y2="0">
      <stop offset="0" stop-color="#d9d2c8"/><stop offset=".3" stop-color="#c9b09a"/><stop offset=".55" stop-color="#e8e2da"/><stop offset=".8" stop-color="#d9a99a"/><stop offset="1" stop-color="#e9ddd4"/>
    </linearGradient>
    <linearGradient id="warm" x1="0" x2="1"><stop offset="0" stop-color="#e07b2f"/><stop offset="1" stop-color="#f6be3c"/></linearGradient>
  </defs>
  <path d="M0 0H1200V590C1050 660 900 705 720 708C470 712 240 640 0 575Z" fill="url(#heroTone)" role="img" aria-label="Photo of a tutor working with a young student at a desk"/>
  <path d="M80 615C300 700 520 720 720 712C900 705 1060 660 1200 590V620C1060 690 900 720 720 722C500 725 290 700 80 615Z" fill="url(#warm)"/>
</svg>
<div class="abs brand"><div class="brand-dot"></div><div class="brand-name">Harbor<br>Scholars LLC</div></div>
<nav class="abs nav"><a class="active">Home</a><a>About us</a><a>Services</a><a>Testimonials</a><a>Team</a><a>Contact</a></nav>
<div class="abs call-btn">
  <svg width="14" height="14" viewBox="0 0 24 24" fill="#fff"><path d="M6.6 10.8a15 15 0 0 0 6.6 6.6l2.2-2.2a1 1 0 0 1 1-.25 11.4 11.4 0 0 0 3.6.57 1 1 0 0 1 1 1V20a1 1 0 0 1-1 1A17 17 0 0 1 3 4a1 1 0 0 1 1-1h3.5a1 1 0 0 1 1 1c0 1.25.2 2.45.57 3.57a1 1 0 0 1-.25 1z"/></svg>
  +1 555 010 2040
</div>
<div class="abs hero-box">
  <div class="kicker">WELCOME TO</div>
  <h1>Harbor Scholars LLC</h1>
  <span class="btn">GET STARTED
    <svg width="14" height="14" viewBox="0 0 20 20"><circle cx="10" cy="10" r="9" fill="#fff"/><path d="M8 6l4 4-4 4" stroke="#e07b2f" stroke-width="2.2" fill="none"/></svg></span>
</div>

<!-- our story -->
<div class="abs vertical-word" style="left:1100px;top:735px;font-size:80px">ABOUT US</div>
<svg class="abs" style="left:130px;top:770px" width="440" height="450" viewBox="0 0 440 450">
  <defs><linearGradient id="storyTone" x1="0" y1="0" x2="1" y2="1"><stop offset="0" stop-color="#bfb4aa"/><stop offset=".5" stop-color="#d6cdc5"/><stop offset="1" stop-color="#eeeae6"/></linearGradient></defs>
  <path d="M210 8A215 215 0 0 0 30 330" stroke="var(--orange)" stroke-width="22" fill="none"/>
  <path d="M405 190A215 215 0 0 1 245 440" stroke="var(--yellow)" stroke-width="26" fill="none"/>
  <circle cx="225" cy="230" r="203" fill="url(#storyTone)" role="img" aria-label="Photo of an online tutor with a headset and laptop"/>
</svg>
<div class="abs story-text">
  <h2>OUR STORY</h2>
  <div class="story-sub">LOREM IPSUM DOLOR SIT AMET,<br>CONSECTETUR ADIPISCING</div>
  <p>RT Marlow, LLC was created to help nonprofits and government contractors meet their basic funding requirements and adopt a Mission Aligned Data Driven mindset that promotes positive change in the lives of the people they serve. Our approach is not simply based off of theoretical business practices, but on practical solutions to real-life situations learned through more than twenty years of experience.</p>
  <span class="btn">LEARN MORE
    <svg width="14" height="14" viewBox="0 0 20 20"><circle cx="10" cy="10" r="9" fill="#fff"/><path d="M8 6l4 4-4 4" stroke="#e07b2f" stroke-width="2.2" fill="none"/></svg></span>
</div>

<!-- why choose us -->
<svg class="abs" style="left:0;top:1255px" width="1200" height="860" viewBox="0 0 1200 860">
  <defs>
    <linearGradient id="desert" x1="0" y1="0" x2="0" y2="1">
      <stop offset="0" stop-color="#6d6a93"/><stop offset=".35" stop-color="#c98a84"/><stop offset=".58" stop-color="#e8b08a"/><stop offset=".75" stop-color="#6b5a3e"/><stop offset="1" stop-color="#3d3526"/>
    </linearGradient>
  </defs>
  <path d="M0 80C300 -10 850 -10 1200 125V20C850 -20 300 -10 0 80Z" fill="url(#warm)" opacity=".95"/>
  <path d="M0 130C300 30 850 20 1200 145V715C850 820 300 820 0 710Z" fill="url(#desert)" role="img" aria-label="Sonoran desert landscape with saguaro cactus at sunset"/>
  <path d="M140 770C420 860 800 860 1120 760C800 845 420 845 140 770Z" fill="url(#warm)" stroke="url(#warm)" stroke-width="6"/>
</svg>
<div class="abs vertical-word" style="left:30px;top:1440px;font-size:80px;color:rgba(255,255,255,.25)">WHY US</div>
<div class="abs why-card" style="left:445px;top:1437px;width:313px;height:171px"><h3>Nemo enim ipsam</h3><p>Lorem ipsum dolor sit amet, consectetur adipiscing elit, sed do eiusmod tempor incididunt ut labore et dolore magna aliqua.</p></div>
<div class="abs why-card" style="left:160px;top:1595px;width:310px;height:178px"><h3>Nemo enim ipsam</h3><p>Lorem ipsum dolor sit amet, consectetur adipiscing elit, sed do eiusmod tempor incididunt ut labore et dolore magna aliqua.</p></div>
<div class="abs why-card" style="left:729px;top:1605px;width:311px;height:178px"><h3>Nemo enim ipsam</h3><p>Lorem ipsum dolor sit amet, consectetur adipiscing elit, sed do eiusmod tempor incididunt ut labore et dolore magna aliqua.</p></div>
<div class="abs why-card" style="left:445px;top:1760px;width:313px;height:171px"><h3>Nemo enim ipsam</h3><p>Lorem ipsum dolor sit amet, consectetur adipiscing elit, sed do eiusmod tempor incididunt ut labore et dolore magna aliqua.</p></div>
<div class="abs why-center" style="left:473px;top:1616px;width:254px;height:136px">WHY CHOOSE<br>US?</div>

<!-- services -->
<div class="abs section-title" style="top:2160px"><div class="ghost">SERVICES</div><h2 style="top:22px">OUR SERVICES</h2></div>

<div class="abs svc" style="left:112px;top:2275px;border-radius:162px 162px 0 0;background:linear-gradient(140deg,#9c8371,#d8c2ad 40%,#8c6f5a 70%,#c9bcae)" role="img" aria-label="Photo of a smiling boy with a tutor"></div>
<div class="abs svc" style="left:112px;top:2585px;background:var(--orange);border-radius:0 0 162px 162px;padding-top:75px">
  <h3>Duis aute irure</h3><p>Lorem ipsum dolor sit amet, consectetur adipiscing elit, sed do eiusmod tempor incididunt ut labore et dolore magna aliqua.</p>
  <svg class="go" viewBox="0 0 20 20"><circle cx="10" cy="10" r="9" fill="#fff"/><path d="M8 6l4 4-4 4" stroke="#e07b2f" stroke-width="2.2" fill="none"/></svg>
</div>

<div class="abs svc" style="left:437px;top:2275px;background:var(--yellow);border-radius:162px 162px 0 0;padding-top:60px">
  <h3>Duis aute irure</h3><p>Lorem ipsum dolor sit amet, consectetur adipiscing elit, sed do eiusmod tempor incididunt ut labore et dolore magna aliqua.</p>
  <svg class="go" viewBox="0 0 20 20"><circle cx="10" cy="10" r="9" fill="#fff"/><path d="M8 6l4 4-4 4" stroke="#f6be3c" stroke-width="2.2" fill="none"/></svg>
</div>
<div class="abs svc" style="left:437px;top:2585px;border-radius:0 0 162px 162px;background:linear-gradient(100deg,#f1ece8,#f3ddd2 45%,#e9e6e2 65%,#6e5446)" role="img" aria-label="Photo of a girl with her tutor at a whiteboard of notes"></div>

<div class="abs svc" style="left:762px;top:2275px;border-radius:162px 162px 0 0;background:linear-gradient(120deg,#c7643a,#d9d3cf 35%,#9aa4b4 60%,#4d5260)" role="img" aria-label="Photo of a student in an online lesson on a laptop"></div>
<div class="abs svc" style="left:762px;top:2585px;background:var(--orange);border-radius:0 0 162px 162px;padding-top:75px">
  <h3>Duis aute irure</h3><p>Lorem ipsum dolor sit amet, consectetur adipiscing elit, sed do eiusmod tempor incididunt ut labore et dolore magna aliqua.</p>
  <svg class="go" viewBox="0 0 20 20"><circle cx="10" cy="10" r="9" fill="#fff"/><path d="M8 6l4 4-4 4" stroke="#e07b2f" stroke-width="2.2" fill="none"/></svg>
</div>

<div class="abs icon-ring" style="left:229px;top:2539px"><svg width="40" height="40" viewBox="0 0 40 40" fill="none" stroke="var(--orange)" stroke-width="2"><circle cx="20" cy="14" r="7"/><path d="M6 34c2-8 8-11 14-11s12 3 14 11"/></svg></div>
<div class="abs icon-ring" style="left:554px;top:2539px"><svg width="40" height="40" viewBox="0 0 40 40" fill="none" stroke="var(--orange)" stroke-width="2"><circle cx="17" cy="17" r="10"/><path d="M25 25l9 9"/></svg></div>
<div class="abs icon-ring" style="left:879px;top:2539px"><svg width="40" height="40" viewBox="0 0 40 40" fill="none" stroke="var(--orange)" stroke-width="2"><path d="M4 10h14v22H4zM22 10h14v22H22z"/><path d="M8 16h6M8 21h6M26 16h6M26 21h6"/></svg></div>

<!-- testimonials -->
<svg class="abs" style="left:0;top:2960px" width="1200" height="660" viewBox="0 0 1200 660">
  <path d="M0 120C300 20 900 10 1200 95V480C900 610 300 610 0 470Z" fill="url(#warm)"/>
  <path d="M160 560C440 650 800 650 1080 545C800 630 440 630 160 560Z" fill="url(#warm)" stroke="url(#warm)" stroke-width="6"/>
</svg>
<div class="abs section-title" style="top:3090px"><div class="ghost" style="color:rgba(255,255,255,.18)">TESTIMONIALS</div><h2 style="top:22px;color:#fff">TESTIMONIALS</h2></div>
<div class="abs t-card" style="left:112px;top:3187px">
  <div class="abs quote-mark">&ldquo;</div>
  <div class="t-head"><div class="avatar" role="img" aria-label="Client portrait"></div><div><h4>Henry</h4><span>Company name</span></div></div>
  <p>Lorem ipsum dolor sit amet, consectetur adipiscing elit, sed do eiusmod tempor incididunt ut labore et dolore magna aliqua. Ut enim ad minim veniam, quis nostrud exercitation ullamco laboris nisi ut aliquip ex ea commodo consequat.</p>
</div>
<div class="abs t-card" style="left:614px;top:3187px">
  <div class="abs quote-mark">&ldquo;</div>
  <div class="t-head"><div class="avatar" role="img" aria-label="Client portrait"></div><div><h4>John doe</h4><span>Company name</span></div></div>
  <p>Lorem ipsum dolor sit amet, consectetur adipiscing elit, sed do eiusmod tempor incididunt ut labore et dolore magna aliqua. Ut enim ad minim veniam, quis nostrud exercitation ullamco laboris nisi ut aliquip ex ea commodo consequat.</p>
</div>
<svg class="abs" style="left:560px;top:3482px" width="80" height="16" viewBox="0 0 80 16">
  <circle cx="8" cy="8" r="6" fill="#fff"/><circle cx="24" cy="8" r="6" fill="#fff"/><circle cx="40" cy="8" r="5" fill="none" stroke="#fff" stroke-width="2"/><circle cx="56" cy="8" r="6" fill="#fff"/><circle cx="72" cy="8" r="6" fill="#fff"/>
</svg>

<!-- team -->
<div class="abs section-title" style="top:3658px"><div class="ghost">OUR TEAM</div><h2 style="top:22px">OUR TEAM</h2></div>
<div class="abs" style="left:599px;top:3780px;width:1px;height:360px;background:#ddd"></div>
<div class="abs member" style="left:226px;top:3830px"><div class="portrait" style="background:linear-gradient(160deg,#e6e3df,#c9b8a8 45%,#8b6e5a 80%,#5e5e66)" role="img" aria-label="Portrait of a team member"></div><h3>John Doe</h3><span>Company name</span></div>
<div class="abs member" style="left:714px;top:3830px"><div class="portrait" style="background:linear-gradient(160deg,#8fa27c,#c9b49a 45%,#e7cdb8 70%,#7a5a46)" role="img" aria-label="Portrait of a team member"></div><h3>John Doe</h3><span>Company name</span></div>

<!-- footer -->
<svg class="abs" style="left:0;top:4200px" width="1200" height="426" viewBox="0 0 1200 426">
  <defs><linearGradient id="earth" x1="0" y1="0" x2="0" y2="1"><stop offset="0" stop-color="#6b3f22"/><stop offset=".4" stop-color="#3a2318"/><stop offset="1" stop-color="#2a170f"/></linearGradient></defs>
  <path d="M0 120C350 20 850 20 1200 110V426H0Z" fill="url(#earth)"/>
  <path d="M0 120C350 20 850 20 1200 110V98C850 5 350 5 0 108Z" fill="url(#warm)"/>
</svg>
<div class="abs" style="left:1110px;top:4050px;width:60px;height:270px;background:linear-gradient(#2a170f,#1a0f0a);opacity:.9;border-radius:30px 30px 0 0" role="img" aria-label="Saguaro cactus silhouette"></div>

<div class="abs foot-col" style="left:113px;top:4355px">
  <h4>QUICK LINKS</h4>
  <ul><li>Home</li><li>About us</li><li>Services</li><li>Blog</li><li>Contact Us</li></ul>
</div>
<div class="abs foot-col" style="left:362px;top:4355px">
  <h4>INFORMATION</h4>
  <ul><li>Terms &amp; Conditions</li><li>Privacy Policy</li><li>Disclaimer</li><li>Site Map</li><li>Contact Us</li></ul>
</div>
<div class="abs foot-col" style="left:625px;top:4355px;width:240px">
  <h4>CONTACT INFO</h4>
  <ul>
    <li><svg width="12" height="12" viewBox="0 0 24 24" fill="#fff"><path d="M6.6 10.8a15 15 0 0 0 6.6 6.6l2.2-2.2a1 1 0 0 1 1-.25 11.4 11.4 0 0 0 3.6.57 1 1 0 0 1 1 1V20a1 1 0 0 1-1 1A17 17 0 0 1 3 4a1 1 0 0 1 1-1h3.5a1 1 0 0 1 1 1c0 1.25.2 2.45.57 3.57a1 1 0 0 1-.25 1z"/></svg>+1 (555) 010-2040</li>
    <li><svg width="12" height="12" viewBox="0 0 24 24" fill="#fff"><path d="M6 2h12v6H6zM3 9h18v8h-3v5H6v-5H3zM8 15v5h8v-5z"/></svg>(555) 010-204</li>
    <li><svg width="12" height="12" viewBox="0 0 24 24" fill="#fff"><path d="M2 5h20v14H2zM3 6l9 7 9-7"/></svg><span style="text-decoration:underline">info@harborscholars.example</span></li>
    <li style="line-height:16px;margin-top:6px"><svg width="12" height="12" viewBox="0 0 24 24" fill="#fff" style="margin-top:2px"><path d="M12 2a7 7 0 0 0-7 7c0 5 7 13 7 13s7-8 7-13a7 7 0 0 0-7-7zm0 9.5A2.5 2.5 0 1 1 12 6.5a2.5 2.5 0 0 1 0 5z"/></svg>#2868 Lorem ipsum dolor sit<br>amet, consectetur</li>
  </ul>
</div>
<div class="abs foot-col" style="left:953px;top:4355px">
  <h4>FOLLOW US</h4>
  <ul class="soc-list"><li><span class="soc"></span>Friendwall</li><li><span class="soc"></span>Chirper</li><li><span class="soc"></span>Circleplus</li><li><span class="soc"></span>Workweb</li></ul>
</div>
<div class="abs copyright">Copyrights © The Company name 2023 | Allrights Reserved</div>

</body>
</html>
```